Korimet Business Cards

Korimet is a software startup and we are looking for business cards that help convey our employee personalities, as well as the professionalism of the company.
Our company font is Comfortaa - and the company logo is attached (we are okay having the text beside the logo if applicable) where we can find the company colour scheme. Cards can be horizontal or vertical format.
We are looking for a two sided business card - on the front we will see the personal details of the employee (name, position, email and phone number), and then on the back, we will see the business details (name and logo, address, phone number, website, email, company tagline: "Accelerating technology disruption in the automotive market")
We want the design to be clean and simple, but also fun, modern, and capturing of a young startup vibe.

```html
<!DOCTYPE html>
<html lang="en">
<head>
<meta charset="utf-8">
<title>Korimet Business Cards</title>
<link rel="stylesheet" href="https://fonts.googleapis.com/css2?family=Comfortaa:wght@400;500;600;700&display=swap">
<style>
  :root {
    --bg: #eeeeee;
    --card: #ffffff;
    --ink: #4b3b99;
    --violet: #4f3f9f;
    --lavender: #ebe8f4;
    --rose-light: #f5e6f0;
    --magenta: #b9519a;
    --photo-text: #eab0d6;
  }
  * { box-sizing: border-box; margin: 0; padding: 0; }
  html, body { width: 1200px; height: 1000px; overflow: hidden; background: var(--bg); }
  body { position: relative; font-family: "Comfortaa", sans-serif; color: var(--ink); }

  .card {
    position: absolute; top: 153px; width: 453px; height: 695px;
    background: var(--card); overflow: hidden;
    box-shadow: 0 2px 8px rgba(0,0,0,0.18);
  }
  .card--company { left: 111px; }
  .card--personal { left: 636px; }

  .card__backdrop { position: absolute; inset: 0; }
  .card--company .card__backdrop {
    background:
      radial-gradient(circle at 24% 0%, var(--lavender) 0, var(--rose-light) 30%, rgba(255,255,255,0) 52%),
      radial-gradient(circle at 79% 93%, var(--lavender) 0, var(--rose-light) 38%, rgba(255,255,255,0) 62%);
  }
  .card--personal .card__backdrop {
    background:
      radial-gradient(circle at 76% 0%, var(--lavender) 0, var(--rose-light) 30%, rgba(255,255,255,0) 52%),
      radial-gradient(circle at 21% 93%, var(--lavender) 0, var(--rose-light) 38%, rgba(255,255,255,0) 62%);
  }

  .brand-name {
    position: absolute; left: 0; right: 0; top: 218px;
    text-align: center; font-size: 64px; font-weight: 700;
    color: var(--violet); letter-spacing: 1px;
  }

  .contact-list { position: absolute; list-style: none; }
  .contact-list li {
    display: flex; align-items: center; gap: 7px;
    height: 48px; font-size: 27px; font-weight: 600; white-space: nowrap;
  }
  .contact-list li.contact-address { font-size: 23px; }
  .contact-icon { width: 32px; height: 32px; flex: none; }
  .card--company .contact-list { left: 50px; top: 354px; }
  .card--personal .contact-list { left: 50px; top: 504px; }
  .card--personal .contact-list li { height: 46px; }

  .tagline {
    position: absolute; left: 0; right: 0; top: 586px;
    text-align: center; font-size: 19px; font-weight: 600; line-height: 23px;
  }

  .photo-slot { position: absolute; left: 123px; top: 102px; width: 206px; height: 206px; }
  .photo-label {
    position: absolute; left: 123px; top: 142px; width: 206px;
    text-align: center; font-size: 36px; line-height: 41px; color: var(--photo-text);
  }
  .name-plate {
    position: absolute; left: 66px; top: 341px; width: 321px; height: 53px;
    background: var(--violet); color: #fff; text-align: center;
    font-size: 44px; font-weight: 600; line-height: 55px; letter-spacing: 1px;
  }
  .job-title {
    position: absolute; left: 0; right: 0; top: 400px;
    text-align: center; font-size: 34px; font-weight: 500;
  }
</style>
</head>
<body>

<svg width="0" height="0" style="position:absolute">
  <defs>
    <symbol id="icon-pin" viewBox="0 0 32 32">
      <circle cx="16" cy="16" r="16" fill="#4f3f9f"/>
      <path d="M16 7a6 6 0 0 0-6 6c0 4.5 6 12 6 12s6-7.5 6-12a6 6 0 0 0-6-6zm0 8.3a2.3 2.3 0 1 1 0-4.6 2.3 2.3 0 0 1 0 4.6z" fill="#fff"/>
    </symbol>
    <symbol id="icon-phone" viewBox="0 0 32 32">
      <circle cx="16" cy="16" r="16" fill="#4f3f9f"/>
      <path d="M11.5 8.5l2.6 3.3-1.6 1.8c.9 2.2 2.5 3.8 4.7 4.7l1.8-1.6 3.3 2.6-1.4 2.6c-5.7-.4-10.2-4.9-10.6-10.6z" fill="#fff"/>
      <path d="M18 9.5a5 5 0 0 1 4.5 4.5M18 6.8a7.7 7.7 0 0 1 7.2 7.2" stroke="#fff" stroke-width="1.4" fill="none"/>
    </symbol>
    <symbol id="icon-globe" viewBox="0 0 32 32">
      <circle cx="16" cy="16" r="16" fill="#4f3f9f"/>
      <g fill="none" stroke="#fff" stroke-width="1.4">
        <circle cx="16" cy="16" r="8.5"/>
        <ellipse cx="16" cy="16" rx="3.8" ry="8.5"/>
        <path d="M7.5 16h17M9 11.5h14M9 20.5h14"/>
      </g>
    </symbol>
    <symbol id="icon-mail" viewBox="0 0 32 32">
      <circle cx="16" cy="16" r="16" fill="#4f3f9f"/>
      <g fill="none" stroke="#fff" stroke-width="1.4" stroke-linejoin="round">
        <path d="M8 14l8-6 8 6v9H8z"/>
        <path d="M8 14l8 5.5 8-5.5M8 23l6-5M24 23l-6-5"/>
      </g>
    </symbol>
  </defs>
</svg>

<section class="card card--company">
  <div class="card__backdrop" role="img" aria-label="Decorative background pattern in soft violet and rose tones"></div>

  <div class="brand-name">korimet</div>

  <ul class="contact-list">
    <li class="contact-address"><svg class="contact-icon"><use href="#icon-pin"/></svg>123 Main Street, City, State</li>
    <li><svg class="contact-icon"><use href="#icon-phone"/></svg>+000 123 456 789</li>
    <li><svg class="contact-icon"><use href="#icon-globe"/></svg>www.yourwebsite.com</li>
    <li><svg class="contact-icon"><use href="#icon-mail"/></svg>username@email.com</li>
  </ul>

  <p class="tagline">Acceleration of technological<br>disruption in the automotive market</p>
</section>

<section class="card card--personal">
  <div class="card__backdrop" role="img" aria-label="Decorative background pattern in soft violet and rose tones"></div>

  <svg class="photo-slot" viewBox="0 0 206 206" role="img" aria-label="Employee portrait photo">
    <circle cx="103" cy="103" r="103" fill="var(--violet)"/>
    <circle cx="103" cy="103" r="88" fill="var(--magenta)"/>
  </svg>
  <div class="photo-label">YOUR<br>PHOTO<br>HERE</div>

  <div class="name-plate">NAME HERE</div>
  <div class="job-title">programmer</div>

  <ul class="contact-list">
    <li><svg class="contact-icon"><use href="#icon-mail"/></svg>username@email.com</li>
    <li><svg class="contact-icon"><use href="#icon-phone"/></svg>+000 123 456 789</li>
  </ul>
</section>

</body>
</html>
```